Decorative concrete business needs new business cards

Our company attracts homeowners and business with disposable cash. We are a artistic decorative coatings company that will transform your driveway, patio, floors or counter tops into a work of art. We also engrave logos and designs right into the concrete! We are upscale and very professional company. I am open for rearranging our logo on the business card and also to different color patterns. We like the blue and black as in BrushNest's logo. We also like blue and orange/yellow.

Target Market(s)

Adults 30-70

Industry/Entity Type

Concrete

Contact Information for Business Card

Simple: Name, phone, email, website and social media icons

Font styles to use
Serif

Colors

Designer to choose colors to be used in the design.

Requirements
Must have
• Must present a professional upscale appearance. I have attached before and after photos that show you what our industry does. Maybe I will have before and after photo on back of card.
Nice to have
• Artistic, but bold. Nothing whimsical or cute.
Should not have
• Should not have cartoon or childlike appearance.

```html
<!DOCTYPE html>
<html lang="en">
<head>
<meta charset="utf-8">
<title>Crestline Surface Arts – Business Cards</title>
<link href="https://fonts.googleapis.com/css2?family=Open+Sans:wght@400;600&display=swap" rel="stylesheet">
<style>
  :root {
    --backdrop: #202020;
    --card: #ffffff;
    --brand-blue: #2a8fc7;
    --ink: #555555;
    --ink-soft: #8a8a8a;
    --social-a: #9b3fa6;
    --social-b: #2a6fb5;
    --social-c: #2a9fd8;
  }
  * { margin: 0; padding: 0; box-sizing: border-box; }
  html, body { width: 1200px; height: 1000px; overflow: hidden; }
  body {
    background: var(--backdrop);
    font-family: "Open Sans", Arial, sans-serif;
    position: relative;
  }
  .card {
    position: absolute;
    left: 320px;
    width: 560px;
    height: 320px;
    background: var(--card);
    border-radius: 26px;
  }
  .card--front { top: 110px; }
  .card--back { top: 520px; }

  .wordmark {
    display: flex;
    align-items: center;
    gap: 12px;
    color: var(--brand-blue);
    font-weight: 600;
    letter-spacing: 1px;
    text-transform: uppercase;
  }
  .wordmark__square {
    width: 30px; height: 30px;
    background: var(--brand-blue);
    flex: none;
  }
  .card--front .wordmark {
    position: absolute;
    left: 50%; top: 50%;
    transform: translate(-50%, -50%);
    font-size: 22px;
    white-space: nowrap;
  }
  .card--back .wordmark {
    position: absolute;
    right: 34px; top: 60px;
    font-size: 15px;
    gap: 9px;
  }
  .card--back .wordmark__square { width: 22px; height: 22px; }

  .holder { position: absolute; left: 40px; top: 118px; }
  .holder__name {
    font-size: 27px; font-weight: 600; color: var(--ink);
    letter-spacing: 0.5px; line-height: 1.1;
  }
  .holder__role {
    font-size: 19px; font-weight: 600; color: var(--brand-blue);
    margin-left: 22px; margin-top: 2px;
  }
  .address {
    position: absolute; left: 62px; top: 196px;
    font-size: 13px; color: var(--ink-soft); line-height: 1.35;
  }
  .contacts {
    position: absolute; left: 40px; top: 236px;
    list-style: none; font-size: 13px; color: var(--ink-soft);
  }
  .contacts li { display: flex; align-items: center; gap: 10px; height: 17px; }
  .contacts svg { width: 11px; height: 11px; fill: var(--brand-blue); flex: none; }
  .contacts .web-accent { color: var(--brand-blue); }
  .follow {
    position: absolute; left: 62px; top: 290px;
    display: flex; align-items: center; gap: 5px;
    font-size: 13px; color: var(--ink-soft);
  }
  .follow__dot { width: 10px; height: 10px; border-radius: 50%; }
  .follow__dot:first-of-type { margin-left: 8px; }
  .dot-a { background: var(--social-a); }
  .dot-b { background: var(--social-b); }
  .dot-c { background: var(--social-c); }
</style>
</head>
<body>
  <section class="card card--front">
    <div class="wordmark"><span class="wordmark__square"></span>Crestline Surface Arts</div>
  </section>

  <section class="card card--back">
    <div class="holder">
      <div class="holder__name">MARCEL STONE</div>
      <div class="holder__role">CEO</div>
    </div>
    <div class="address">Your Street Address,<br>Singapore, 1234</div>
    <ul class="contacts">
      <li>
        <svg viewBox="0 0 24 24"><path d="M6.6 10.8a15 15 0 0 0 6.6 6.6l2.2-2.2c.3-.3.7-.4 1-.2 1.1.4 2.3.6 3.6.6.6 0 1 .4 1 1V20c0 .6-.4 1-1 1A17 17 0 0 1 3 4c0-.6.4-1 1-1h3.5c.6 0 1 .4 1 1 0 1.3.2 2.5.6 3.6.1.3 0 .7-.2 1z"/></svg>
        <span style="margin-left:12px">+000 123 456 789</span>
      </li>
      <li>
        <svg viewBox="0 0 24 24"><path d="M2 5h20v14H2zm2 2v.5l8 5 8-5V7z"/></svg>
        <span style="margin-left:12px">yourname@email.com</span>
      </li>
      <li>
        <svg viewBox="0 0 24 24"><path d="M12 2a10 10 0 1 0 0 20 10 10 0 0 0 0-20zm-1 2.1V8H7.3A8 8 0 0 1 11 4.1zM13 4.1A8 8 0 0 1 16.7 8H13zM4.6 10H11v4H4.6a8 8 0 0 1 0-4zm8.4 0h6.4a8 8 0 0 1 0 4H13zM7.3 16H11v3.9A8 8 0 0 1 7.3 16zm5.7 0h3.7a8 8 0 0 1-3.7 3.9z"/></svg>
        <span style="margin-left:12px">www.<span class="web-accent">websitename</span>.com</span>
      </li>
    </ul>
    <div class="follow">Follow On
      <span class="follow__dot dot-a"></span>
      <span class="follow__dot dot-b"></span>
      <span class="follow__dot dot-c"></span>
    </div>
    <div class="wordmark"><span class="wordmark__square"></span>Crestline Surface Arts</div>
  </section>
</body>
</html>
```